Business Card Design Project

Business card, that is serious, yet elegant/upscale
Using both sides though only one for information
A space for a QR code would be good
basic contact details.
I will upload company logo
Updates

Thanks everyone who has submitted so far.  No additional designs are needed at this time, We could easily select from one of the many that are currebtly shown.

If you have a design in already and it is still listed it is in the running. Do not submit anymore, choosing now is hard enough given the talent and creativity shared.  WE are making a chpice today this evening.

Again thank you all.

Target Market(s)

CIo's, VP's and people at large companies

Industry/Entity Type

Business

Requirements
Must have
• The business card needs the basic ingo like:
The transparent gear/log enlarged on the card has been well received so is now a must forthe wining design

Name
Title

417 W. Ferncourt
#2870
Chicago,Il 60601
Tel #

contact@brivanto-mail.example
Nice to have
• A QR Code, no glaring, but usable.

Should not have
• no cursive/handwriting fonts.

```html
<!DOCTYPE html>
<html lang="en">
<head>
<meta charset="utf-8">
<title>Brivanto Group – Business Card</title>
<link href="https://fonts.googleapis.com/css2?family=Open+Sans:wght@400;600;700&display=swap" rel="stylesheet">
<style>
  :root {
    --backdrop: #050505;
    --card: #ffffff;
    --brand-green: #2ed119;
    --ink: #55585b;
    --rule: #6a6d70;
    --faint: #e9eaea;
  }
  * { margin: 0; padding: 0; box-sizing: border-box; }
  html, body { width: 1200px; height: 900px; overflow: hidden; }
  body {
    background: var(--backdrop);
    font-family: "Open Sans", Arial, sans-serif;
    position: relative;
  }
  .card {
    position: absolute;
    left: 244px;
    width: 712px;
    height: 406px;
    background: var(--card);
    overflow: hidden;
  }
  .card--front { top: 31px; }
  .card--back { top: 465px; }

  .faint-emblem {
    position: absolute;
    left: -120px;
    top: -60px;
    width: 380px;
    height: 380px;
    border-radius: 50%;
    background: var(--faint);
  }

  .brand { position: absolute; }
  .brand__mark {
    position: absolute;
    left: 0; top: 0;
    width: 78px; height: 78px;
    border-radius: 50%;
    background: var(--brand-green);
  }
  .brand__name {
    position: absolute;
    left: 104px; top: 6px;
    font-size: 38px;
    font-weight: 600;
    letter-spacing: -1px;
    color: var(--brand-green);
    white-space: nowrap;
    line-height: 1;
  }
  .brand__rule {
    position: absolute;
    left: 108px; top: 66px;
    width: 98px; height: 1.5px;
    background: var(--brand-green);
  }
  .brand__tagline {
    position: absolute;
    left: 212px; top: 57px;
    font-size: 13.5px;
    color: var(--brand-green);
    white-space: nowrap;
    letter-spacing: 0.3px;
  }
  .card--front .brand { left: 314px; top: 276px; }
  .card--back .brand { left: 38px; top: 42px; }

  .holder { position: absolute; left: 38px; top: 199px; }
  .holder__name {
    font-size: 22px; font-weight: 700; color: var(--ink); line-height: 1.1;
  }
  .holder__title {
    font-size: 13.5px; color: var(--brand-green); margin-top: 2px;
  }

  .contact-rule {
    position: absolute;
    left: 38px; top: 322px;
    width: 636px; height: 1.5px;
    background: var(--rule);
  }
  .contact {
    position: absolute;
    top: 334px;
    font-size: 13px;
    color: var(--ink);
    line-height: 18.5px;
  }
  .contact__row { display: flex; align-items: center; white-space: nowrap; }
  .contact__row--indent { padding-left: 27px; }
  .contact__icon { width: 15px; height: 15px; margin-right: 12px; flex: none; }
  .contact--address { left: 38px; }
  .contact--phone { left: 274px; }
  .contact--online { left: 460px; }
</style>
</head>
<body>
  <section class="card card--front">
    <div class="faint-emblem" role="img" aria-label="Large faint company emblem"></div>
    <div class="brand">
      <div class="brand__mark"></div>
      <div class="brand__name">Brivanto Group</div>
      <div class="brand__rule"></div>
      <div class="brand__tagline">software + service</div>
    </div>
  </section>

  <section class="card card--back">
    <div class="brand">
      <div class="brand__mark"></div>
      <div class="brand__name">Brivanto Group</div>
      <div class="brand__rule"></div>
      <div class="brand__tagline">software + service</div>
    </div>

    <div class="holder">
      <div class="holder__name">Marek Holloway</div>
      <div class="holder__title">President/CEO</div>
    </div>

    <div class="contact-rule"></div>

    <div class="contact contact--address">
      <div class="contact__row">
        <svg class="contact__icon" viewBox="0 0 15 15" aria-hidden="true"><rect width="15" height="15" rx="2" fill="var(--brand-green)"/><path d="M7.5 2.5a3.2 3.2 0 0 0-3.2 3.2c0 2.4 3.2 6.3 3.2 6.3s3.2-3.9 3.2-6.3a3.2 3.2 0 0 0-3.2-3.2z" fill="#fff"/><circle cx="7.5" cy="5.7" r="1.2" fill="var(--brand-green)"/></svg>
        417 W. Ferncourt #2870
      </div>
      <div class="contact__row contact__row--indent">Chicago, Il 60601</div>
    </div>

    <div class="contact contact--phone">
      <div class="contact__row">
        <svg class="contact__icon" viewBox="0 0 15 15" aria-hidden="true"><rect width="15" height="15" rx="2" fill="var(--brand-green)"/><circle cx="7.5" cy="7.5" r="4.6" fill="#fff"/><path d="M5.8 5.2l1 .9-.5.8c.4.8.9 1.3 1.7 1.7l.8-.5.9 1-.7.7c-1.8-.3-3.4-1.9-3.7-3.7z" fill="var(--brand-green)"/></svg>
        070.482.316
      </div>
      <div class="contact__row">
        <svg class="contact__icon" viewBox="0 0 15 15" aria-hidden="true"><rect width="15" height="15" rx="2" fill="var(--brand-green)"/><rect x="4.5" y="2.5" width="6" height="10" rx="1" fill="#fff"/><rect x="5.5" y="3.8" width="4" height="5" fill="var(--brand-green)"/></svg>
        070.537.904
      </div>
    </div>

    <div class="contact contact--online">
      <div class="contact__row">
        <svg class="contact__icon" viewBox="0 0 15 15" aria-hidden="true"><rect width="15" height="15" rx="2" fill="var(--brand-green)"/><rect x="3" y="4.5" width="9" height="6" fill="#fff"/><path d="M3 4.5l4.5 3.5 4.5-3.5" fill="none" stroke="var(--brand-green)" stroke-width="1"/></svg>
        contact@brivanto-mail.example
      </div>
      <div class="contact__row">
        <svg class="contact__icon" viewBox="0 0 15 15" aria-hidden="true"><rect width="15" height="15" rx="2" fill="var(--brand-green)"/><circle cx="7.5" cy="7.5" r="4.5" fill="#fff"/><path d="M3 7.5h9M7.5 3c-2 2.5-2 6.5 0 9M7.5 3c2 2.5 2 6.5 0 9" fill="none" stroke="var(--brand-green)" stroke-width="0.8"/></svg>
        www.brivanto-group.example
      </div>
    </div>
  </section>
</body>
</html>
```